Business Card Design

We need a new business card design for a CPA office that has been in business for over 10 years. We are a Accounting Concierge firm that offers the following services: Certified Public Accountant, Personal & Business Tax Preparation, Accounting, Bookkeeping, Payroll Services, Tax Litigation Services.
Certified LedgerNest CertPartner.  We would like to see designs that use the color navy blue in the company logo with classic accent colors.  We would like the card to be on a textured high pound card stock and that is more classic and less modern in design.  The final design should communicate class and professionalism.

Reason: I gave feedback to many of the designers with some changes.  Please re-read the brief as we would like to remove the photo of the man on the card.  We also want only light grey or white background, not navy or blue - the navy or blue tones should be the font or accent colors.  Please also, consider creating a logo with the initials P&W or PW or P&W CPA.

Industry/Entity Type
Business
Contact Information for Business Card
Pellford & Company CPA, Dominic Pellford III, 4317 Larkmoor Road, Suite D, Bradenton, FL  34519, Phone: (941) 555-0137, Fax: (941) 555-0182, Email: Dominic@DPellfordCPA.example, Website: www.DPellfordCPA.example
Requirements
Must have
- LedgerNest Logo

Should not have
- we no longer want the photo on the card.

```html
<!DOCTYPE html>
<html lang="en">
<head>
<meta charset="utf-8">
<title>Pellford &amp; Company CPA — Business Card</title>
<link rel="stylesheet" href="https://fonts.googleapis.com/css2?family=Cinzel:wght@400;500&family=Arimo:wght@400;700&display=swap">
<style>
  :root {
    --stage: #e9e8ec;
    --card: #ffffff;
    --navy: #1e2a5a;
    --navy-text: #243a8c;
    --band-edge: #c9ccd8;
    --rule: #c8c8cc;
    --badge: #f4c21a;
  }
  * { box-sizing: border-box; margin: 0; padding: 0; }
  html, body { width: 1200px; height: 800px; overflow: hidden; }
  body {
    background: var(--stage);
    display: flex;
    align-items: center;
    justify-content: center;
    font-family: "Arimo", Arial, sans-serif;
  }
  .business-card {
    position: relative;
    width: 875px;
    height: 500px;
    background: var(--card);
    box-shadow: 0 6px 24px rgba(30, 42, 90, 0.18);
  }
  .name-band {
    position: absolute;
    left: 0;
    top: 52px;
    width: 100%;
    height: 82px;
    background: var(--navy);
    border-top: 3px solid var(--band-edge);
    border-bottom: 3px solid var(--band-edge);
    display: flex;
    align-items: center;
    justify-content: center;
  }
  .firm-name {
    font-family: "Cinzel", "Times New Roman", serif;
    font-weight: 400;
    font-size: 46px;
    letter-spacing: 1px;
    color: #ffffff;
  }
  .firm-name .firm-suffix { font-size: 30px; margin-left: 4px; }
  .partner-badge {
    position: absolute;
    left: 62px;
    top: 200px;
    width: 180px;
    height: 180px;
  }
  .contact-block {
    position: absolute;
    left: 455px;
    top: 188px;
    color: var(--navy-text);
  }
  .person-name {
    font-weight: 700;
    font-size: 25px;
    letter-spacing: 0.3px;
    margin-left: 38px;
    margin-bottom: 14px;
  }
  .contact-list {
    list-style: none;
    border-left: 1.5px solid var(--rule);
    padding-left: 14px;
    padding-top: 4px;
    padding-bottom: 4px;
  }
  .contact-item {
    display: flex;
    align-items: flex-start;
    font-size: 20px;
    line-height: 27px;
  }
  .contact-item.is-primary { font-weight: 700; }
  .contact-icon {
    width: 18px;
    height: 18px;
    margin-top: 4px;
    margin-right: 14px;
    flex: none;
    fill: var(--navy-text);
  }
</style>
</head>
<body>
  <article class="business-card">
    <header class="name-band">
      <h1 class="firm-name">PELLFORD &amp; COMPANY<span class="firm-suffix">CPA</span></h1>
    </header>

    <svg class="partner-badge" viewBox="0 0 180 180" role="img" aria-label="Certified LedgerNest CertPartner badge">
      <circle cx="90" cy="90" r="86" fill="var(--badge)"/>
    </svg>

    <section class="contact-block">
      <h2 class="person-name">DOMINIC PELLFORD III</h2>
      <ul class="contact-list">
        <li class="contact-item is-primary">
          <svg class="contact-icon" viewBox="0 0 24 24" aria-hidden="true"><path d="M6.6 10.8a15.1 15.1 0 0 0 6.6 6.6l2.2-2.2c.3-.3.7-.4 1-.2 1.1.4 2.3.6 3.6.6.6 0 1 .4 1 1V20c0 .6-.4 1-1 1A17 17 0 0 1 3 4c0-.6.4-1 1-1h3.5c.6 0 1 .4 1 1 0 1.3.2 2.5.6 3.6.1.3 0 .7-.2 1z"/></svg>
          <span>941-555-0137</span>
        </li>
        <li class="contact-item">
          <svg class="contact-icon" viewBox="0 0 24 24" aria-hidden="true"><path d="M6 3h10v5H6zM4 9h16a2 2 0 0 1 2 2v8H2v-8a2 2 0 0 1 2-2zm2 4v2h4v-2zm0 3v1h4v-1zm10-3a1 1 0 1 0 0 2 1 1 0 0 0 0-2z"/></svg>
          <span>941-555-0182</span>
        </li>
        <li class="contact-item">
          <svg class="contact-icon" viewBox="0 0 24 24" aria-hidden="true"><path d="M3 5h18v14H3zm2 2v.5l7 4.5 7-4.5V7zm0 2.8V17h14V9.8l-7 4.5z"/></svg>
          <span>Dominic@DPellfordCPA.example</span>
        </li>
        <li class="contact-item">
          <svg class="contact-icon" viewBox="0 0 24 24" aria-hidden="true"><path d="M12 2a10 10 0 1 0 0 20 10 10 0 0 0 0-20zm6.9 6h-3a15 15 0 0 0-1.3-3.9A8 8 0 0 1 18.9 8zM12 4c.8 1.2 1.5 2.5 1.9 4h-3.8c.4-1.5 1.1-2.8 1.9-4zM4.3 14a8 8 0 0 1 0-4h3.4a16 16 0 0 0 0 4zm.8 2h3a15 15 0 0 0 1.3 3.9A8 8 0 0 1 5.1 16zm3-8h-3a8 8 0 0 1 4.3-3.9C8.8 5.3 8.4 6.6 8.1 8zM12 20c-.8-1.2-1.5-2.5-1.9-4h3.8c-.4 1.5-1.1 2.8-1.9 4zm2.3-6H9.7a14 14 0 0 1 0-4h4.6a14 14 0 0 1 0 4zm.3 5.9c.6-1.2 1-2.5 1.3-3.9h3a8 8 0 0 1-4.3 3.9zm1.7-5.9a16 16 0 0 0 0-4h3.4a8 8 0 0 1 0 4z"/></svg>
          <span>www.DPellfordCPA.example</span>
        </li>
        <li class="contact-item">
          <svg class="contact-icon" viewBox="0 0 24 24" aria-hidden="true"><path d="M12 2a7 7 0 0 0-7 7c0 5.2 7 13 7 13s7-7.8 7-13a7 7 0 0 0-7-7zm0 9.5a2.5 2.5 0 1 1 0-5 2.5 2.5 0 0 1 0 5z"/></svg>
          <span>4317 Larkmoor Road, Suite D,<br>Bradenton, FL 34519</span>
        </li>
      </ul>
    </section>
  </article>
</body>
</html>
```